We need a DL size flyer, double sided, for our lawn mowing and gardening business, Kestrel Yards.

We want to run on the front side, the following promotion:
50% off lawn mowing, applies to first lawn mowed on any regular service,
applies to first 100 callers only, so call now!
Professional lawn mowing at an affordable price.

Logo at the bottom left, with Lawn and Garden Maintenance written just below logo.

On bottom Right contact details;
Tom and Gareth
Ph: 0487650912
Email: kestrelyards@mailbox-demo.com
www.kestrelyards-demo.com.au

Front side positioned horizontally, with a bright and colour full design in the background, with the offer of 50% Off lawn mowing in large letters along the top.

On the rear side, also positioned horizontally, a list of our services, stating;

At Kestrel Yards we specialise in the following services;
Lawn mowing
Edging
Blowing
Hedging
Pruning
Tree Loping
Weeding
Poisoning
Mulching
Fertilising
Rubbish removal
Planting
Lawn care and advice
Turf
And any other garden maintenance job,
No job too big or too small.
(No particular order, whatever fits best)
Also include our contact details,
Kestrel Yards
Ph 0487650912
www.kestrelyards-demo.com.au

Target Market(s)

Home owners, aged between 30-50 years old, moderate socio ecenomic status to more afluent areas.

Industry/Entity Type

Business

Requirements
Must have
• DL size, front and back, full colour.
Nice to have
• The writting stating "Kestrel Yards" in our logo is quite bland, if that could also be amended to make it more appealing, but change the writting design only not the actual logo.

```html
<!DOCTYPE html>
<html lang="en">
<head>
<meta charset="utf-8">
<title>Kestrel Yards – DL Flyer</title>
<link rel="stylesheet" href="https://fonts.googleapis.com/css2?family=Anton&family=Lato:ital,wght@0,700;0,900;1,700;1,900&display=swap">
<style>
  :root {
    --promo-yellow: #fde60a;
    --promo-red: #e41b1b;
    --sky-deep: #5fb0e0;
    --sky-light: #d9f0fa;
    --grass-bright: #a6dc2f;
    --grass-mid: #4fb51c;
    --grass-deep: #2b6a12;
    --soil: #1c1712;
    --white: #ffffff;
    --footer-grey: #6d6d6d;
    --logo-green: #1f6f1c;
    --ink: #1b1b1b;
  }
  * { margin: 0; padding: 0; box-sizing: border-box; }
  html, body { width: 1173px; height: 1200px; overflow: hidden; background: var(--white); }
  body { position: relative; font-family: "Lato", sans-serif; }

  .side { position: absolute; left: 0; width: 1173px; overflow: hidden; }
  .side--front { top: 0; height: 586px; }
  .side--back { top: 618px; height: 582px; }

  .scene {
    position: absolute; left: 0; width: 100%;
    background: linear-gradient(180deg,
      var(--sky-deep) 0%, var(--sky-light) 30%,
      var(--grass-bright) 40%, var(--grass-mid) 62%,
      var(--grass-deep) 80%, var(--soil) 92%, var(--soil) 100%);
  }
  .side--front .scene { top: 104px; height: 482px; }
  .side--back .scene {
    top: 0; height: 542px;
    background: linear-gradient(180deg,
      var(--sky-deep) 0%, var(--sky-light) 18%,
      var(--grass-bright) 24%, var(--grass-mid) 38%,
      var(--grass-deep) 48%, var(--soil) 56%, var(--soil) 100%);
  }

  .promo-band {
    position: absolute; top: 0; left: 0; width: 100%; height: 104px;
    background: var(--promo-yellow);
  }
  .promo-headline {
    position: absolute; top: -6px; left: 0; width: 100%;
    text-align: center; font-family: "Anton", sans-serif;
    font-size: 98px; line-height: 112px; letter-spacing: 1px;
    color: var(--promo-red);
    text-shadow: 2px 2px 0 #7a0c0c;
  }

  .tagline {
    position: absolute; top: 116px; left: 28px;
    font-style: italic; font-weight: 700; font-size: 33px; line-height: 36px;
    color: var(--white);
    text-shadow: 0 0 3px #2c4f63, 1px 1px 2px #2c4f63;
  }
  .offer-terms {
    position: absolute; top: 110px; right: 30px; text-align: right;
    font-style: italic; font-weight: 900; font-size: 23px; line-height: 32px;
    color: var(--promo-yellow);
    text-shadow: 0 0 3px #3a3a00, 1px 1px 2px #3a3a00;
  }
  .offer-terms .call-now {
    display: block; margin-top: 4px;
    font-size: 38px; line-height: 44px; color: var(--promo-red);
    text-shadow: 0 0 3px var(--white), 0 0 3px var(--white);
  }

  .brand { position: absolute; left: 0; width: 100%; text-align: center; }
  .brand-mark {
    display: inline-flex; align-items: center; gap: 14px;
    font-weight: 900; color: var(--white);
  }
  .brand-mark .dot { border-radius: 50%; background: var(--logo-green); }
  .brand-sub {
    display: block; font-weight: 900; color: var(--promo-yellow);
    text-shadow: 0 0 3px var(--ink), 1px 1px 2px var(--ink);
  }
  .side--front .brand { top: 290px; }
  .side--front .brand-mark { font-size: 64px; }
  .side--front .brand-mark .dot { width: 54px; height: 54px; }
  .side--front .brand-sub { margin-top: 70px; font-size: 34px; line-height: 38px; }

  .side--back .brand { top: 140px; }
  .side--back .brand-mark { font-size: 38px; }
  .side--back .brand-mark .dot { width: 32px; height: 32px; }
  .side--back .brand-sub { margin-top: 22px; font-size: 21px; line-height: 22px; }

  .contact-line {
    position: absolute; top: 544px; left: 0; width: 100%;
    text-align: center; font-weight: 700; font-size: 20px; color: var(--white);
    word-spacing: 1px;
  }

  .no-job {
    position: absolute; top: 22px; right: 28px;
    font-style: italic; font-weight: 700; font-size: 32px; color: var(--white);
  }
  .services-heading {
    position: absolute; top: 298px; left: 0; width: 100%; text-align: center;
    font-style: italic; font-weight: 900; font-size: 28px; color: var(--promo-red);
    text-shadow: 0 0 2px var(--white), 0 0 2px var(--white), 0 0 2px var(--white);
  }
  .services {
    position: absolute; top: 358px; left: 122px;
    display: grid; grid-template-columns: 230px 226px 230px 300px;
    grid-auto-flow: column; grid-template-rows: repeat(4, 41px);
    list-style: none; font-weight: 700; font-size: 21px; color: var(--white);
  }
  .services li::before { content: "• "; }
  .services li.services-more {
    grid-row: 3 / span 2; font-style: italic; font-size: 20px; line-height: 26px;
  }
  .services li.services-more::before { content: ""; }

  .footer-bar {
    position: absolute; bottom: 0; left: 0; width: 100%; height: 40px;
    background: var(--footer-grey);
    text-align: center; font-weight: 700; font-size: 22px; line-height: 40px;
    color: var(--white); word-spacing: 2px;
  }
</style>
</head>
<body>

<section class="side side--front">
  <div class="scene" role="img" aria-label="Photo of tall bright green grass against a blue sky with dark soil below"></div>
  <div class="promo-band"><h1 class="promo-headline">50% OFF LAWNMOWING!</h1></div>

  <p class="tagline">Professional lawn mowing<br>at an affordable price</p>
  <p class="offer-terms">
    ...applies to first lawn mowed<br>
    on any regular service<br>
    applies to first 100 callers only
    <span class="call-now">so call now!</span>
  </p>

  <div class="brand">
    <span class="brand-mark"><span class="dot"></span>KESTREL YARDS</span>
    <span class="brand-sub">LAWN &amp; GARDEN<br>MAINTENANCE</span>
  </div>

  <p class="contact-line">Tom and Gareth &nbsp;-&nbsp; Ph: 0487650912 &nbsp;-&nbsp; Email: kestrelyards@mailbox-demo.com &nbsp;-&nbsp; www.kestrelyards-demo.com.au</p>
</section>

<section class="side side--back">
  <div class="scene" role="img" aria-label="Photo of tall bright green grass against a blue sky with dark soil below"></div>

  <p class="no-job">...No job too big or too small!</p>

  <div class="brand">
    <span class="brand-mark"><span class="dot"></span>KESTREL YARDS</span>
    <span class="brand-sub">LAWN &amp; GARDEN<br>MAINTENANCE</span>
  </div>

  <h2 class="services-heading">At Kestrel Yards we specialise in the following services:</h2>
  <ul class="services">
    <li>Lawn mowing</li>
    <li>Edging</li>
    <li>Blowing</li>
    <li>Hedging</li>
    <li>Pruning</li>
    <li>Tree Loping</li>
    <li>Weeding</li>
    <li>Poisoning</li>
    <li>Mulching</li>
    <li>Fertilising</li>
    <li>Rubbish removal</li>
    <li>Planting</li>
    <li>Lawn care and advice</li>
    <li>Turf</li>
    <li class="services-more">...and any other<br>garden maintenance job</li>
  </ul>

  <div class="footer-bar">Phone: 0487650912 &nbsp; - &nbsp; www.kestrelyards-demo.com.au</div>
</section>

</body>
</html>
```